Kestrel Works Business Cards

This job is for the design of a business card.
I would like to review the design in 2x colour tones to choose from black and white inverted.
EG:
Black with white logo and white with black logo on BACK
White with black text on front and black with white text options
PRINTING DIMENSIONS: 4.5 x 8.5cm
Complete design will need to be provided in ready to print format with bleed lines
Target Market(s)
The audience of my business are people in the trade industry.
It will be also used for general networking with trades people and possible future clients.
I want to be represented as a professional, dynamic, creative and personable operator.
The card should reflect style, taste, experience, professionalism.
Industry/Entity Type
Business
Requirements
Must have
- BACK CONTENT:
- Logo in white and black background and vice versa with WHITE card and black logo review samples.
- FRONT CARD CONTENT:
- Name: Morgan Telvane
- Director
- Phone: 0438 216 947
- Email: morgan@kestrelworks.com.au
- Web: kestrelworks.com.au
- LICENCE #: KT-R 72158
Nice to have
- Possibly a textured background design on rear as a pose to a solid black
- Possibly adding a blue or orange discreet colour tone (possibly for email, phone abbreviated letter or symbols).

```html
<!DOCTYPE html>
<html lang="en">
<head>
<meta charset="utf-8">
<title>Kestrel Works — Business Card Front</title>
<link rel="stylesheet" href="https://fonts.googleapis.com/css2?family=Arimo:ital,wght@0,400;0,700;1,700&display=swap">
<style>
  :root {
    --ink: #111111;
    --paper: #ffffff;
    --steel-dark: #3c3c3c;
    --steel-mid: #8a8a8a;
    --steel-light: #f2f2f2;
    --mark-grey: #8e8e8e;
  }
  * { margin: 0; padding: 0; box-sizing: border-box; }
  html, body { width: 1200px; height: 2276px; overflow: hidden; background: var(--paper); }
  .card {
    position: relative;
    width: 1200px;
    height: 2276px;
    background: var(--paper);
    font-family: "Arimo", Arial, sans-serif;
    color: var(--ink);
    overflow: hidden;
  }
  .top-band {
    position: absolute; left: 0; top: 0; width: 1200px; height: 400px;
    background:
      linear-gradient(180deg, rgba(255,255,255,0.75) 0, rgba(255,255,255,0.75) 44px, rgba(255,255,255,0) 48px),
      linear-gradient(90deg, var(--steel-dark) 0%, var(--steel-mid) 30%, var(--steel-light) 62%, var(--steel-mid) 85%, var(--steel-dark) 100%);
  }
  .brand-bar {
    position: absolute; left: 0; top: 392px; width: 1100px; height: 136px;
    background: var(--ink);
  }
  .brand-name {
    position: absolute; left: 70px; top: 392px; height: 136px;
    display: flex; align-items: center;
    font-size: 118px; font-weight: 400; letter-spacing: -2px;
    color: var(--paper); text-transform: uppercase; line-height: 1;
  }
  .tagline {
    position: absolute; left: 272px; top: 584px;
    font-size: 42px; letter-spacing: 15px; font-weight: 400; line-height: 1;
  }
  .contact { position: absolute; left: 272px; top: 760px; width: 900px; }
  .contact .name { font-size: 76px; font-weight: 700; font-style: italic; line-height: 1; }
  .contact .title { margin-top: 16px; font-size: 40px; line-height: 1; }
  .contact .address { margin-top: 40px; font-size: 52px; line-height: 72px; }
  .contact .label { margin-top: 36px; font-size: 42px; font-weight: 700; font-style: italic; line-height: 1; }
  .contact .phone { margin-top: 14px; font-size: 62px; font-weight: 700; letter-spacing: 2px; line-height: 1; }
  .contact .online { margin-top: 28px; font-size: 42px; line-height: 60px; }
  .contact .licence { margin-top: 30px; font-size: 38px; line-height: 1; }
  .bottom-band {
    position: absolute; left: 0; top: 1568px; width: 1200px; height: 708px;
    background: linear-gradient(90deg, #7a7a7a 0%, #cfcfcf 30%, #f7f7f7 55%, #d4d4d4 80%, #8c8c8c 100%);
  }
  .initials { position: absolute; left: 0; top: 0; width: 1200px; height: 2276px; }
  .initials text { font-family: "Arimo", Arial, sans-serif; fill: var(--mark-grey); }
</style>
</head>
<body>
  <main class="card">
    <div class="top-band"></div>
    <div class="brand-bar"></div>
    <div class="brand-name">Kestrel Works</div>
    <div class="tagline">CONSTRUCTION GROUP</div>

    <section class="contact">
      <p class="name">Morgan Telvane</p>
      <p class="title">Director</p>
      <p class="address">0000 South Main Street, Suite #1<br>City here, State here, 000000</p>
      <p class="label">Phone</p>
      <p class="phone">0438 216 947</p>
      <p class="online">morgan@kestrelworks.com.au<br>kestrelworks.com.au</p>
      <p class="licence">LICENCE #: KT-R 72158</p>
    </section>

    <div class="bottom-band"></div>
    <svg class="initials" viewBox="0 0 1200 2276" aria-hidden="true">
      <text x="240" y="2240" font-size="860" textLength="880" lengthAdjust="spacingAndGlyphs">KW</text>
    </svg>
  </main>
</body>
</html>
```